New Business Card Design Project

The idea, the card is to put a card, which contains two companies at the same time. Please see the attached data and idea of how the current cards are.
VELMIR
Constructora
Ferrepiezas Caliza SRL.
Equipos para Plantas de Tratamientos y Acueductos, Alquiler de Equipos Pesados para la Construcción.
C / Tomás Urbina No.47
Barrio Lucero, Santo Domingo. República Dominicana.
Tel .: 1809 512 4476
CEL: 1829 746 2158
oriol@ferrepiezascaliza.example
velmirconstrution@correo-ejemplo.example
www.ferrepiezascaliza.example
Velmir construction.
Es una empresa constructora.
NOTA: La idea es llevar una sola tarjeta para dos compañías. o si no resulta hacer un diseño en cada lado, uno para cada empresa.Equipos para Plantas de Tratamiento y Acueductos, Alquiler de Equipos Pesados para la Construcción.
Deben de llevar, los logos.
VELMIR
Constructora
Ferrepiezas Caliza SRL.
C / Tomás Urbina No.47
Tel .: 1809 512 4476
CEL: 1829 746 2158
Velmir construction.
VELMIR
Constructora
Ferrepiezas Caliza SRL.
C / Tomás Urbina No.47
Tel .: 1809 512 4476
CEL: 1829 746 2158
Velmir construction.
It is a construction company
NOTE: The idea is to carry a single card for two companies. or if it does not turn out to make a design on each side, one for each company. Equipment for Treatment Plants and Aqueducts, Rental of Heavy Equipment for Construction.
They must carry, the logos.
How is the design similar to that, send example, for data, from previous designs.
What I'm looking for is a new design, not a remodeled copy
ferrepiezascaliza
Tel: 1809 542 4476
cel: 1829 746 2158
oriol@gerrepiezascaliza.example
Direccion:
C/ Tomás Urbina # 47
Barrio lucero, Santo Domingo
Republica Dominicana
Velmir
constructora
Tel: 1809 358-1047
Cel: 1829 746 2158
velmirsa1@correo-ejemplo.example
Direccion:
C/ Tomás Urbina # 47
Republica Dominicana
FERREPIEZAS CALIZA, S.R.L.
C/ Ramiro Olmedo Lasta esquina Tomás Urbina # 47
Barrio Lucero, Santo Domingo, República Dominicana
Office: 809.542.4476
Fax: 809.594.7361
Cel (Local): 829 746 2158
E-mail: MUESTRA@MUESTRA.example
E-mail:MUESTRA@correo-ejemplo.example
Website: http://www.MUESTRA.example

```html
<!DOCTYPE html>
<html lang="es">
<head>
<meta charset="utf-8">
<title>Velmir Constructora – Tarjeta de presentación</title>
<link rel="stylesheet" href="https://fonts.googleapis.com/css2?family=Work+Sans:wght@400;500;600;800&display=swap">
<style>
  :root {
    --stage: #1b1b1b;
    --card: #262626;
    --card-edge: #2e2e2e;
    --ink: #f4f4f4;
    --accent: #ee6a2a;
    --emboss: #3d3d3d;
    --emboss-light: #4a4a4a;
  }
  * { margin: 0; padding: 0; box-sizing: border-box; }
  html, body {
    width: 1200px; height: 900px; overflow: hidden;
    background: var(--stage);
    font-family: "Work Sans", Arial, sans-serif;
  }
  .sheet {
    width: 1200px; height: 900px;
    display: flex; flex-direction: column; align-items: center; justify-content: center;
    gap: 24px;
  }
  .card {
    position: relative;
    width: 760px; height: 420px;
    background: linear-gradient(160deg, var(--card-edge), var(--card));
    box-shadow: 0 10px 30px rgba(0,0,0,.5);
  }
  /* front side */
  .card--front { display: flex; align-items: center; justify-content: center; }
  .brand { display: flex; align-items: center; gap: 16px; }
  .brand__mark { width: 56px; height: 56px; }
  .brand__name {
    font-weight: 800; font-size: 76px; letter-spacing: 1px; line-height: 1;
  }
  .card--front .brand__mark { background: var(--emboss); }
  .card--front .brand__name { color: var(--emboss-light); }

  /* back side */
  .card--back { display: flex; align-items: center; }
  .card--back .brand { position: absolute; left: 48px; top: 170px; gap: 12px; }
  .card--back .brand__mark { width: 44px; height: 44px; background: var(--accent); }
  .card--back .brand__name { font-size: 58px; color: var(--ink); }
  .divider {
    position: absolute; left: 368px; top: 40px;
    width: 2px; height: 340px; background: var(--ink);
  }
  .contact {
    position: absolute; left: 392px; top: 40px;
    color: var(--ink); font-size: 15.5px; letter-spacing: .6px; line-height: 23px;
  }
  .contact__name {
    color: var(--accent); font-size: 24px; font-weight: 500;
    letter-spacing: 3.5px; line-height: 26px;
  }
  .contact__role { margin-bottom: 8px; }
  .contact__company { color: var(--accent); font-weight: 600; }
  .contact__address { margin-bottom: 6px; }
  .contact__list { list-style: none; }
  .contact__list li { display: flex; align-items: center; gap: 10px; }
  .contact__list--web { margin-top: 6px; }
  .icon { width: 13px; height: 13px; flex: none; }
  .icon path, .icon rect, .icon circle { stroke: var(--accent); fill: none; stroke-width: 1.6; }
  .icon .solid { fill: var(--accent); stroke: none; }
</style>
</head>
<body>
<main class="sheet">
  <section class="card card--front" aria-label="Cara frontal">
    <div class="brand">
      <span class="brand__mark"></span>
      <span class="brand__name">VELMIR</span>
    </div>
  </section>

  <section class="card card--back" aria-label="Cara posterior">
    <div class="brand">
      <span class="brand__mark"></span>
      <span class="brand__name">VELMIR</span>
    </div>
    <span class="divider"></span>
    <div class="contact">
      <p class="contact__name">ADRIÁN SOLANO</p>
      <p class="contact__role">Director</p>
      <p class="contact__company">FERREPIEZAS CALIZA, S.R.L.</p>
      <p class="contact__address">C/ Ramiro Olmedo Lasta<br>esquina Tomás Urbina # 47<br>Barrio Lucero, Santo Domingo,<br>República Dominicana</p>
      <ul class="contact__list">
        <li><svg class="icon" viewBox="0 0 14 14"><path d="M3 1 L5 4 L4 6 Q6 9 8 10 L10 9 L13 11 L11 13 Q3 11 1 3 Z"/></svg>809.542.4476</li>
        <li><svg class="icon" viewBox="0 0 14 14"><rect class="solid" x="3" y="1" width="8" height="4"/><rect class="solid" x="1" y="5" width="12" height="6" rx="1"/><rect x="4" y="9" width="6" height="4"/></svg>809.594.7361</li>
        <li><svg class="icon" viewBox="0 0 14 14"><rect x="3.5" y="1" width="7" height="12" rx="1"/><circle class="solid" cx="7" cy="11" r=".9"/></svg>829 746 2158</li>
      </ul>
      <ul class="contact__list contact__list--web">
        <li><svg class="icon" viewBox="0 0 14 14"><rect x="1" y="3" width="12" height="8"/><path d="M1 3 L7 8 L13 3"/></svg>muestra@muestra.example</li>
        <li><svg class="icon" viewBox="0 0 14 14"><rect x="1" y="3" width="12" height="8"/><path d="M1 3 L7 8 L13 3"/></svg>muestra@correo-ejemplo.example</li>
        <li><svg class="icon" viewBox="0 0 14 14"><circle cx="7" cy="7" r="6"/><path d="M1 7 H13 M7 1 Q3 7 7 13 M7 1 Q11 7 7 13"/></svg>www.muestra.example</li>
      </ul>
    </div>
  </section>
</main>
</body>
</html>
```